Increased budget: GUI redesign: 10 year old user interface needs modern look-and-feel

UPDATE: Please DO look at more than only th eone image I attached! Almost all designs are simply reworks of that one picture. That is not what we are looking for. Check out the video to understand what the product does, and try to make something better.
We have an existing app (see https://www.vornatek.com/downloadTunePilot.php?vers=3_9_1_140964&dir=Vornatek_OEM/3_9_1_140964&name=DSP_Control_Software) which needs refreshing. See also a video here: https://vornatek-oem.com/software/ and the user manual attached here. The GUI is now 800x400 pixels, which is too small; and not scalable, which will be fixed in the future. We need a new, modern look-and-feel, and images that can be exported from the design in various sizes. The current design is attached as well as a collection of PNG files. The overall layout can stay similar, although we are open to good ideas for improvements. The design should be targeted at professional users, not end users; the product is used by audio professionals (e.g. sound engineers, loudspeaker designers). Also see our web version: https://www.vornatek.com/tunepilot/skins/1_1_2/container.html?MAC=Demo%201x2
The winner will also be asked to do a full design of the application GUI (based on the design done here), with several more windows etc, and additional payment depending on the work to be done.

Target Market(s)

Professional audio

Industry/Entity Type

Audio / Industrial

Font styles to use
Other font styles liked:
• Futura (not mandatory)

Colors

Designer to choose colors to be used in the design.

Requirements
Must have
• Modern, timeless design, not too bling bling
Nice to have
• Flat design
Should not have
• 3D, bling bling, many colours, etc

```html
<!DOCTYPE html>
<html lang="en">
<head>
<meta charset="utf-8">
<title>DSP Control – Color version</title>
<link href="https://fonts.googleapis.com/css2?family=Jost:wght@400;500;600;700&display=swap" rel="stylesheet">
<style>
:root{
  --page:#ffffff;
  --window:#222327;
  --rail:#1a1b1e;
  --panel:#242529;
  --panel-line:#33353a;
  --nav:#1b1c1f;
  --card:#1d1e21;
  --field:#34363b;
  --field-text:#e8e8e8;
  --check:#76787d;
  --gold:#c9a66b;
  --gold-text:#d1ad6c;
  --text:#f2f2f2;
  --muted:#bfc0c3;
  --green:#4fd05a;
  --groove:#111214;
  --grid:#3a3c41;
}
*{box-sizing:border-box;margin:0;padding:0}
html,body{width:1200px;height:610px;overflow:hidden;background:var(--page)}
body{font-family:"Jost",sans-serif;position:relative;color:var(--text)}
.title{position:absolute;left:26px;top:20px;font-size:17px;font-weight:700;color:#111}
.window{position:absolute;left:232px;top:78px;width:731px;height:479px;border-radius:28px;background:var(--window);overflow:hidden;box-shadow:0 14px 30px rgba(0,0,0,.25)}
.rail{position:absolute;left:0;top:0;width:41px;height:100%;background:var(--rail)}
.lights{position:absolute;left:13px;top:12px;display:flex;gap:4px}
.lights i{width:5px;height:5px;border-radius:50%;display:block}
.brand{position:absolute;left:9px;top:32px;width:24px;height:24px;border-radius:5px;background:#17324a;display:flex;align-items:center;justify-content:center;font-size:5.3px;font-weight:500;color:#fff}
.rail-icon{position:absolute;left:13px;width:14px;height:14px}
.sep-v{position:absolute;left:169px;top:14px;width:1px;height:450px;background:var(--panel-line)}
.nav{position:absolute;left:58px;width:97px;height:33px;border-radius:9px;background:var(--nav);display:flex;align-items:center;font-size:8.5px;font-weight:600;color:var(--text)}
.nav svg{position:absolute;left:14px;width:16px;height:16px}
.nav span{position:absolute;left:42px}
.nav.active{background:var(--gold)}
.nav-rule{position:absolute;left:63px;width:87px;height:1px;background:var(--panel-line)}
.panel{position:absolute;left:178px;top:31px;width:541px;height:437px;border:1px solid var(--panel-line);border-radius:14px;background:var(--panel)}
.label{position:absolute;font-size:7.5px;font-weight:600;color:var(--gold-text)}
.hdr{position:absolute;font-size:5.6px;font-weight:500;color:var(--muted)}
.field{position:absolute;height:15px;border-radius:2px;background:var(--field);font-size:5.6px;font-weight:600;color:var(--field-text);display:flex;align-items:center;padding-left:6px}
.field.select::after{content:"";position:absolute;right:5px;top:5px;border-left:4px solid transparent;border-right:4px solid transparent;border-top:5px solid #fff}
.check{position:absolute;width:10px;height:10px;border-radius:2px;background:var(--check)}
.check.on{background:var(--green)}
.qbox{position:absolute;height:7px;border:1px solid #8b8d92;border-radius:3px}
.qbox::after{content:"";position:absolute;left:10px;top:0;width:4px;height:4px;border:1px solid #ddd;border-radius:50%}
.card{position:absolute;top:275px;width:50px;height:150px;border-radius:7px;background:var(--card)}
.card .label{width:100%;text-align:center;top:7px;white-space:nowrap}
.card .field{left:8px;width:36px;justify-content:center;padding:0}
.card .field.select{justify-content:flex-start;padding-left:6px}
.card .knob{position:absolute;left:0;top:30px}
.tag{position:absolute;width:100%;text-align:center;top:121px;font-size:7px;font-weight:600;color:var(--gold-text)}
.small{position:absolute;font-size:5.5px;font-weight:600;color:var(--text)}
svg.art{position:absolute;left:0;top:0}
</style>
</head>
<body>
<div class="title">#3 Color version</div>

<div class="window">
  <aside class="rail">
    <div class="lights"><i style="background:#ff5f57"></i><i style="background:#febc2e"></i><i style="background:#28c840"></i></div>
    <div class="brand">Vornatek</div>
    <svg class="rail-icon" style="top:434px" viewBox="0 0 14 14"><rect x="1" y="2.5" width="12" height="9" rx="2.5" fill="#5a5c61"/><path d="M3 5l4 3 4-3" stroke="#1a1b1e" stroke-width="1.2" fill="none"/></svg>
    <svg class="rail-icon" style="top:470px;display:none" viewBox="0 0 14 14"></svg>
  </aside>
  <svg class="rail-icon" style="top:355px" viewBox="0 0 14 14"><rect x="1" y="2.5" width="12" height="9" rx="2.5" fill="#5a5c61"/><path d="M3 5l4 3 4-3" stroke="#1a1b1e" stroke-width="1.2" fill="none"/></svg>
  <svg class="rail-icon" style="top:391px" viewBox="0 0 14 14"><circle cx="7" cy="7" r="6" fill="#5a5c61"/><text x="7" y="9.8" font-size="8" font-weight="700" text-anchor="middle" fill="#1a1b1e" font-family="Jost,sans-serif">?</text></svg>
  <svg class="rail-icon" style="top:427px" viewBox="0 0 14 14"><circle cx="7" cy="7" r="4.6" fill="none" stroke="#5a5c61" stroke-width="3.2" stroke-dasharray="2 1.6"/><circle cx="7" cy="7" r="3.6" fill="#5a5c61"/><circle cx="7" cy="7" r="1.6" fill="#1a1b1e"/></svg>

  <div class="sep-v"></div>

  <nav>
    <div class="nav" style="top:30px"><svg viewBox="0 0 16 16"><rect x="1" y="1" width="6" height="6" rx="1.5" fill="var(--gold)"/><rect x="9" y="1" width="6" height="6" rx="1.5" fill="var(--gold)"/><rect x="1" y="9" width="6" height="6" rx="1.5" fill="var(--gold)"/><rect x="10" y="10" width="4" height="5" rx="1.2" fill="var(--gold)"/></svg><span>Main</span></div>
    <div class="nav" style="top:71px"><svg viewBox="0 0 16 16"><rect x="1" y="2" width="14" height="5" rx="2" fill="var(--gold)"/><rect x="1" y="9" width="14" height="5" rx="2" fill="var(--gold)"/><rect x="3" y="4" width="4" height="1" fill="var(--nav)"/><rect x="3" y="11" width="4" height="1" fill="var(--nav)"/></svg><span>X - Over</span></div>
    <div class="nav-rule" style="top:114px"></div>
    <div class="nav" style="top:125px"><svg viewBox="0 0 16 16"><rect x="1" y="5" width="14" height="10" rx="3" fill="var(--gold)"/><path d="M8 1v8M5 6.5L8 9.5 11 6.5" stroke="var(--nav)" stroke-width="1.4" fill="none"/></svg><span>In 01</span></div>
    <div class="nav" style="top:165px"><svg viewBox="0 0 16 16"><rect x="1" y="5" width="14" height="10" rx="3" fill="var(--gold)"/><path d="M8 1v8M5 6.5L8 9.5 11 6.5" stroke="var(--nav)" stroke-width="1.4" fill="none"/></svg><span>In 02</span></div>
    <div class="nav" style="top:205px"><svg viewBox="0 0 16 16"><rect x="1" y="5" width="14" height="10" rx="3" fill="var(--gold)"/><path d="M8 1v8M5 6.5L8 9.5 11 6.5" stroke="var(--nav)" stroke-width="1.4" fill="none"/></svg><span>In 03</span></div>
    <div class="nav" style="top:245px"><svg viewBox="0 0 16 16"><rect x="1" y="5" width="14" height="10" rx="3" fill="var(--gold)"/><path d="M8 1v8M5 6.5L8 9.5 11 6.5" stroke="var(--nav)" stroke-width="1.4" fill="none"/></svg><span>In 04</span></div>
    <div class="nav-rule" style="top:288px"></div>
    <div class="nav active" style="top:299px"><svg viewBox="0 0 16 16"><rect x="1" y="5" width="14" height="10" rx="3" fill="#fff"/><path d="M8 10V1M5 3.5L8 0.8 11 3.5" stroke="var(--gold)" stroke-width="1.4" fill="none"/></svg><span>Out 01</span></div>
    <div class="nav" style="top:339px"><svg viewBox="0 0 16 16"><rect x="1" y="5" width="14" height="10" rx="3" fill="var(--gold)"/><path d="M8 10V1M5 3.5L8 0.8 11 3.5" stroke="var(--nav)" stroke-width="1.4" fill="none"/></svg><span>Out 02</span></div>
    <div class="nav" style="top:378px"><svg viewBox="0 0 16 16"><rect x="1" y="5" width="14" height="10" rx="3" fill="var(--gold)"/><path d="M8 10V1M5 3.5L8 0.8 11 3.5" stroke="var(--nav)" stroke-width="1.4" fill="none"/></svg><span>Out 03</span></div>
    <div class="nav" style="top:418px"><svg viewBox="0 0 16 16"><rect x="1" y="5" width="14" height="10" rx="3" fill="var(--gold)"/><path d="M8 10V1M5 3.5L8 0.8 11 3.5" stroke="var(--nav)" stroke-width="1.4" fill="none"/></svg><span>Out 04</span></div>
  </nav>

  <section class="panel">
    <svg class="art" width="539" height="435" viewBox="0 0 539 435" font-family="Jost,sans-serif">
      <defs>
        <pattern id="minor" width="4" height="4.2" patternUnits="userSpaceOnUse" y="43"><rect width="4" height="0.6" fill="#55575c"/></pattern>
        <pattern id="minorGain" width="4" height="4.2" patternUnits="userSpaceOnUse" y="41"><rect width="4" height="0.6" fill="#55575c"/></pattern>
        <pattern id="grid" width="27.2" height="20.5" patternUnits="userSpaceOnUse" x="191" y="24"><path d="M0 0H27.2M0 0V20.5" stroke="var(--grid)" stroke-width="0.6" fill="none"/></pattern>
        <pattern id="meter" width="12" height="2" patternUnits="userSpaceOnUse"><rect width="12" height="0.8" fill="#8a6a34"/></pattern>
        <linearGradient id="capG" x1="0" x2="1"><stop offset="0" stop-color="#8a6a34"/><stop offset=".5" stop-color="#e3c78b"/><stop offset="1" stop-color="#8a6a34"/></linearGradient>
        <g id="cap"><rect x="-5" y="-9" width="10" height="18" rx="4" fill="url(#capG)" stroke="#5d4520" stroke-width=".6"/><path d="M-3 -5H3M-3 -2.5H3M-3 0H3M-3 2.5H3M-3 5H3" stroke="#5d4520" stroke-width=".6"/></g>
      </defs>

      <!-- mixer -->
      <g font-size="4" fill="#ddd" font-weight="600">
        <text x="11" y="45">10</text><text x="13" y="65">5</text><text x="13" y="85">0</text><text x="12" y="106">-5</text><text x="10" y="146">-10</text>
        <text x="172" y="45">10</text><text x="173" y="65">5</text><text x="173" y="85">0</text><text x="172" y="106">-5</text><text x="171" y="146">-10</text>
      </g>
      <g stroke="#d0d0d0" stroke-width=".8">
        <path d="M20 43H31M20 63H31M20 83H31M20 104H31M20 124H31M20 144H31M20 165H31"/>
        <path d="M58 43H68M58 63H68M58 83H68M58 104H68M58 124H68M58 144H68M58 165H68"/>
        <path d="M94 43H104M94 63H104M94 83H104M94 104H104M94 124H104M94 144H104M94 165H104"/>
        <path d="M132 43H143M132 63H143M132 83H143M132 104H143M132 124H143M132 144H143M132 165H143"/>
        <path d="M156 43H167M156 63H167M156 83H167M156 104H167M156 124H167M156 144H167M156 165H167"/>
      </g>
      <rect x="24" y="43" width="7" height="122" fill="url(#minor)"/>
      <rect x="60" y="43" width="7" height="122" fill="url(#minor)"/>
      <rect x="96" y="43" width="7" height="122" fill="url(#minor)"/>
      <rect x="135" y="43" width="7" height="122" fill="url(#minor)"/>
      <g fill="var(--groove)">
        <rect x="35" y="40" width="5" height="133" rx="2"/><rect x="72" y="40" width="5" height="133" rx="2"/>
        <rect x="108" y="40" width="5" height="133" rx="2"/><rect x="147" y="40" width="5" height="133" rx="2"/>
      </g>
      <use href="#cap" x="37.5" y="104"/><use href="#cap" x="74.5" y="163"/><use href="#cap" x="110.5" y="163"/><use href="#cap" x="149.5" y="163"/>
      <g font-size="7" fill="var(--gold-text)" font-weight="600" text-anchor="middle">
        <text x="36" y="185">1</text><text x="74" y="185">2</text><text x="112" y="185">3</text><text x="149" y="185">4</text>
      </g>

      <!-- response graph -->
      <rect x="183" y="15" width="296" height="190" rx="7" fill="#1d1e21"/>
      <rect x="191" y="24" width="272" height="164" fill="url(#grid)" stroke="#55575c" stroke-width=".6"/>
      <path d="M325 106Q336 104 341 84Q345 62 345 65Q346 62 349 84Q354 104 369 106Z" fill="#1f3fb0"/>
      <line x1="191" y1="106" x2="463" y2="106" stroke="#fff" stroke-width="1"/>
      <g font-size="4" fill="#ddd" font-weight="600">
        <text x="470" y="27">15</text><text x="470" y="53">10</text><text x="471" y="81">5</text><text x="471" y="107">0</text><text x="470" y="135">-5</text><text x="469" y="161">-10</text><text x="469" y="190">-15</text>
        <text x="192" y="200">10</text><text x="220" y="200">20</text><text x="255" y="200">50</text><text x="284" y="200">100</text><text x="310" y="200">200</text><text x="338" y="200">500</text><text x="362" y="200">1K</text><text x="391" y="200">5K</text><text x="417" y="200">10K</text><text x="444" y="200">20K</text>
      </g>
      <g font-size="4.2" font-weight="700" text-anchor="middle">
        <circle cx="220" cy="106" r="3.6" fill="#c9a66b"/><text x="220" y="107.6" fill="#222">1</text>
        <circle cx="245" cy="106" r="3.6" fill="#e8305a"/><text x="245" y="107.6" fill="#222">2</text>
        <circle cx="270" cy="106" r="3.6" fill="#e5c21a"/><text x="270" y="107.6" fill="#222">3</text>
        <circle cx="295" cy="106" r="3.6" fill="#2fd06a"/><text x="295" y="107.6" fill="#222">4</text>
        <circle cx="320" cy="106" r="3.6" fill="#22c8e8"/><text x="320" y="107.6" fill="#222">5</text>
        <circle cx="345" cy="65" r="3.6" fill="#2a50ff"/><text x="345" y="66.6" fill="#fff">6</text>
        <circle cx="370" cy="106" r="3.6" fill="#5a2ae8"/><text x="370" y="107.6" fill="#fff">7</text>
        <circle cx="395" cy="106" r="3.6" fill="#b02ae8"/><text x="395" y="107.6" fill="#fff">8</text>
        <circle cx="420" cy="106" r="3.6" fill="#e8203a"/><text x="420" y="107.6" fill="#fff">9</text>
        <circle cx="445" cy="106" r="3.6" fill="#c9a66b"/><text x="445" y="107.3" fill="#222" font-size="3.4">10</text>
      </g>

      <!-- output gain -->
      <g stroke="#d0d0d0" stroke-width=".8">
        <path d="M489 41H499M489 61H499M489 142H499M489 163H499M489 183H499M489 197H499"/>
        <path d="M511 41H522M511 61H522M511 142H522M511 163H522M511 183H522M511 197H522"/>
      </g>
      <rect x="490" y="41" width="9" height="160" fill="url(#minorGain)"/>
      <rect x="512" y="41" width="9" height="160" fill="url(#minorGain)"/>
      <rect x="489" y="81" width="10" height="41" fill="url(#meter)"/>
      <rect x="511" y="81" width="10" height="41" fill="url(#meter)"/>
      <rect x="503" y="37" width="5" height="167" rx="2" fill="var(--groove)"/>
      <use href="#cap" x="505.5" y="101"/>

      <line x1="358" y1="225" x2="358" y2="426" stroke="var(--panel-line)"/>
    </svg>

    <div class="label" style="left:17px;top:20px">Mixer</div>
    <div class="label" style="left:483px;top:20px">Gain</div>
    <div class="field" style="left:16px;top:190px;width:36px">0.00</div>
    <div class="field" style="left:55px;top:190px;width:36px">Mute</div>
    <div class="field" style="left:94px;top:190px;width:36px">Mute</div>
    <div class="field" style="left:133px;top:190px;width:36px">Mute</div>

    <div class="label" style="left:13px;top:226px">Peq</div>
    <div class="hdr" style="left:12px;top:243px">On</div><div class="hdr" style="left:33px;top:243px">Type</div><div class="hdr" style="left:84px;top:243px">Freq</div><div class="qbox" style="left:119px;top:245px;width:25px"></div><div class="hdr" style="left:151px;top:243px">Gain</div>
    <div class="hdr" style="left:189px;top:243px">On</div><div class="hdr" style="left:210px;top:243px">Type</div><div class="hdr" style="left:261px;top:243px">Freq</div><div class="qbox" style="left:296px;top:245px;width:25px"></div><div class="hdr" style="left:328px;top:243px">Gain</div>

    <div class="peq">
      <div class="check" style="left:13px;top:260px"></div><div class="field select" style="left:28px;top:257px;width:49px">Bell</div><div class="field" style="left:82px;top:257px;width:34px">20Hz</div><div class="field" style="left:119px;top:257px;width:25px">1.0</div><div class="field" style="left:147px;top:257px;width:26px">0.00</div>
      <div class="check" style="left:13px;top:282px"></div><div class="field select" style="left:28px;top:279px;width:49px">Bell</div><div class="field" style="left:82px;top:279px;width:34px">40Hz</div><div class="field" style="left:119px;top:279px;width:25px">1.0</div><div class="field" style="left:147px;top:279px;width:26px">0.00</div>
      <div class="check" style="left:13px;top:305px"></div><div class="field select" style="left:28px;top:302px;width:49px">Bell</div><div class="field" style="left:82px;top:302px;width:34px">80Hz</div><div class="field" style="left:119px;top:302px;width:25px">1.0</div><div class="field" style="left:147px;top:302px;width:26px">0.00</div>
      <div class="check" style="left:13px;top:327px"></div><div class="field select" style="left:28px;top:324px;width:49px">Bell</div><div class="field" style="left:82px;top:324px;width:34px">160Hz</div><div class="field" style="left:119px;top:324px;width:25px">1.0</div><div class="field" style="left:147px;top:324px;width:26px">0.00</div>
      <div class="check" style="left:13px;top:349px"></div><div class="field select" style="left:28px;top:346px;width:49px">Bell</div><div class="field" style="left:82px;top:346px;width:34px">320Hz</div><div class="field" style="left:119px;top:346px;width:25px">1.0</div><div class="field" style="left:147px;top:346px;width:26px">0.00</div>

      <div class="check" style="left:190px;top:260px"></div><div class="field select" style="left:205px;top:257px;width:49px">Bell</div><div class="field" style="left:259px;top:257px;width:34px">20Hz</div><div class="field" style="left:296px;top:257px;width:25px">1.0</div><div class="field" style="left:324px;top:257px;width:26px">0.00</div>
      <div class="check" style="left:190px;top:282px"></div><div class="field select" style="left:205px;top:279px;width:49px">Bell</div><div class="field" style="left:259px;top:279px;width:34px">40Hz</div><div class="field" style="left:296px;top:279px;width:25px">1.0</div><div class="field" style="left:324px;top:279px;width:26px">0.00</div>
      <div class="check" style="left:190px;top:305px"></div><div class="field select" style="left:205px;top:302px;width:49px">Bell</div><div class="field" style="left:259px;top:302px;width:34px">80Hz</div><div class="field" style="left:296px;top:302px;width:25px">1.0</div><div class="field" style="left:324px;top:302px;width:26px">0.00</div>
      <div class="check" style="left:190px;top:327px"></div><div class="field select" style="left:205px;top:324px;width:49px">Bell</div><div class="field" style="left:259px;top:324px;width:34px">160Hz</div><div class="field" style="left:296px;top:324px;width:25px">1.0</div><div class="field" style="left:324px;top:324px;width:26px">0.00</div>
      <div class="check" style="left:190px;top:349px"></div><div class="field select" style="left:205px;top:346px;width:49px">Bell</div><div class="field" style="left:259px;top:346px;width:34px">320Hz</div><div class="field" style="left:296px;top:346px;width:25px">1.0</div><div class="field" style="left:324px;top:346px;width:26px">0.00</div>
    </div>

    <div class="label" style="left:13px;top:370px">HPF</div>
    <div class="check on" style="left:14px;top:394px"></div>
    <div class="field" style="left:28px;top:391px;width:49px">OFF</div>
    <div class="field select" style="left:82px;top:391px;width:91px">Linkwitz-Riley 24dB</div>
    <div class="label" style="left:190px;top:370px">LPF</div>
    <div class="check on" style="left:191px;top:394px"></div>
    <div class="field" style="left:205px;top:391px;width:49px">OFF</div>
    <div class="field select" style="left:259px;top:391px;width:91px">Linkwitz-Riley 24dB</div>

    <div class="check" style="left:385px;top:242px"></div><div class="small" style="left:398px;top:243px">MUTE</div>
    <div class="check" style="left:435px;top:242px"></div><div class="small" style="left:447px;top:243px">INVERT</div>
    <div class="field" style="left:488px;top:240px;width:36px;justify-content:center;padding:0">0.00dB</div>

    <div class="card" style="left:366px">
      <div class="label">Delay</div>
      <svg class="knob" width="50" height="52" viewBox="-25 -26 50 52"><circle r="19" fill="none" stroke="#9a9ca0" stroke-width="2.6" stroke-dasharray=".6 2"/><circle r="15.5" fill="#141414"/><circle r="14" fill="#c9a25a"/><circle r="10" fill="#d8b87a"/><rect x="19" y="-.6" width="4" height="1.2" fill="#d8433a"/><rect x="1" y="19" width="3" height="1" fill="#d8433a"/></svg>
      <div class="field" style="top:97px">0.0</div>
      <div class="field select" style="top:118px">ms</div>
    </div>
    <div class="card" style="left:424px">
      <div class="label">Limiter</div>
      <svg class="knob" width="50" height="52" viewBox="-25 -26 50 52"><circle r="19" fill="none" stroke="#9a9ca0" stroke-width="2.6" stroke-dasharray=".6 2"/><circle r="15.5" fill="#141414"/><circle r="14" fill="#c9a25a"/><circle r="10" fill="#d8b87a"/><rect x="19" y="-.6" width="4" height="1.2" fill="#d8433a"/><rect x="1" y="19" width="3" height="1" fill="#d8433a"/></svg>
      <div class="field" style="top:97px">224Vpk</div>
      <div class="tag">THR</div>
    </div>
    <div class="card" style="left:480px">
      <div class="label">Compresor</div>
      <svg class="knob" width="50" height="52" viewBox="-25 -26 50 52"><circle r="19" fill="none" stroke="#9a9ca0" stroke-width="2.6" stroke-dasharray=".6 2"/><circle r="15.5" fill="#141414"/><circle r="14" fill="#c9a25a"/><circle r="10" fill="#d8b87a"/><rect x="19" y="-.6" width="4" height="1.2" fill="#d8433a"/><rect x="1" y="19" width="3" height="1" fill="#d8433a"/></svg>
      <div class="field" style="top:97px">50 db/s</div>
      <div class="tag">REL</div>
    </div>
  </section>
</div>
</body>
</html>
```